qTorvix - A forward thinking technology company in the greater Silicon Valley

A .ppt slide deck for a software consulting company. This slide deck will be used for project kick off meetings, sales proposals, and presentations to large audiences that report progress on a variety of projects. It should catch the eye with appealing creativity. Allow for flexibility in space and display. Project well both virtually and in person under varying light conditions. The finished product should give the impression that we are a custom shop but balance in appeal to larger, more traditional companies.

Review of the designs has been delayed due to holiday travel. Thank you for your submissions. I look forward to getting back to you the week of December 3rd.

Target Market(s)

We are an innovative technology company in the greater Silicon Valley. We design and build custom business analytics tools for large, retail corporations. Our solutions deal primarily in the supply chain space but we are leaning towards commercial construction and telecommunications industries. We are targeting prospective clients interested in machine learning and artificial intelligence. Our customers know quality and will pay for a custom solution that exceeds their expectations.

Industry/Entity Type

Business Software

Font styles to use
Sans Serif

Colors

Designer to choose colors to be used in the design.

Requirements
Must have
• Color, graphics, and photos. Multiple different template pages to appeal for graphs, pictures, text, or timelines.
Should not have
• Anything that resembles a "fidget spinner."

```html
<!DOCTYPE html>
<html lang="en">
<head>
<meta charset="UTF-8">
<title>qTorvix – Charts and Graphics</title>
<link href="https://fonts.googleapis.com/css2?family=Montserrat:wght@400;500;700;800&display=swap" rel="stylesheet">
<style>
  :root {
    --bg: #ffffff;
    --ink: #0d0d0d;
    --muted: #6b6b6b;
    --track: #f1f1f1;
    --accent: #9bc35a;
    --corner: #f6f6f6;
    --brand: #4a4a4a;
  }
  * { margin: 0; padding: 0; box-sizing: border-box; }
  html, body { width: 1200px; height: 675px; overflow: hidden; background: var(--bg); }
  body { font-family: "Montserrat", Arial, sans-serif; color: var(--ink); }
  .slide { position: relative; width: 1200px; height: 675px; overflow: hidden; background: var(--bg); }
  .slide-decor { position: absolute; inset: 0; }
  .brand {
    position: absolute; left: 34px; top: 28px;
    display: flex; align-items: center; gap: 8px;
    font-size: 13px; font-weight: 700; letter-spacing: 1px; color: var(--brand);
  }
  .brand-mark { width: 10px; height: 10px; background: var(--accent); }
  .site-link {
    position: absolute; right: 80px; top: 29px;
    font-size: 11px; color: var(--muted);
  }
  .page-number {
    position: absolute; right: 38px; top: 29px;
    font-size: 11px; color: var(--muted);
  }
  .slide-title {
    position: absolute; top: 106px; left: 0; width: 100%;
    text-align: center; font-size: 43px; font-weight: 800; letter-spacing: 0.5px;
  }
  .stat { position: absolute; top: 254px; width: 226px; text-align: center; }
  .stat-ring { position: relative; width: 226px; height: 226px; }
  .stat-ring svg { width: 226px; height: 226px; display: block; }
  .stat-value {
    position: absolute; inset: 0; display: flex; align-items: center; justify-content: center;
    font-size: 45px; font-weight: 800;
  }
  .stat-label {
    margin-top: 41px; font-size: 24px; font-weight: 800; letter-spacing: 0.3px;
    white-space: nowrap;
  }
  .prompt {
    position: absolute; left: 41px; top: 583px;
    transform: rotate(-90deg); transform-origin: left top;
    font-size: 9px; color: var(--muted); letter-spacing: 0.3px; white-space: nowrap;
  }
  .mouse-icon { position: absolute; left: 36px; top: 602px; }
</style>
</head>
<body>
<main class="slide">
  <svg class="slide-decor" width="1200" height="675" viewBox="0 0 1200 675" aria-hidden="true">
    <polygon points="0,0 274,0 0,254" fill="var(--corner)"/>
    <polygon points="1090,675 1200,563 1200,675" fill="var(--accent)"/>
    <line x1="1172" y1="24" x2="1200" y2="2" stroke="#dcdcdc" stroke-width="1"/>
  </svg>

  <div class="brand"><span class="brand-mark"></span>qTorvix</div>
  <div class="site-link">www.qtorvixlabs.com</div>
  <div class="page-number">11</div>

  <h1 class="slide-title">CHARTS AND GRAPHICS</h1>

  <section class="stat" style="left:97px">
    <div class="stat-ring">
      <svg viewBox="0 0 226 226" aria-hidden="true">
        <circle cx="113" cy="113" r="107" fill="none" stroke="var(--track)" stroke-width="6"/>
        <circle cx="113" cy="113" r="107" fill="none" stroke="var(--accent)" stroke-width="6" pathLength="100" stroke-dasharray="70 100" transform="rotate(-90 113 113)"/>
      </svg>
      <div class="stat-value">70</div>
    </div>
    <div class="stat-label">DISCUSS</div>
  </section>

  <section class="stat" style="left:352px">
    <div class="stat-ring">
      <svg viewBox="0 0 226 226" aria-hidden="true">
        <circle cx="113" cy="113" r="107" fill="none" stroke="var(--track)" stroke-width="6"/>
        <circle cx="113" cy="113" r="107" fill="none" stroke="var(--accent)" stroke-width="6" pathLength="100" stroke-dasharray="90 100" transform="rotate(-90 113 113)"/>
      </svg>
      <div class="stat-value">90</div>
    </div>
    <div class="stat-label">PRODUCTION</div>
  </section>

  <section class="stat" style="left:617px">
    <div class="stat-ring">
      <svg viewBox="0 0 226 226" aria-hidden="true">
        <circle cx="113" cy="113" r="107" fill="none" stroke="var(--track)" stroke-width="6"/>
        <circle cx="113" cy="113" r="107" fill="none" stroke="var(--accent)" stroke-width="6" pathLength="100" stroke-dasharray="30 100" transform="rotate(-90 113 113)"/>
      </svg>
      <div class="stat-value">30</div>
    </div>
    <div class="stat-label">RESEARCH</div>
  </section>

  <section class="stat" style="left:871px">
    <div class="stat-ring">
      <svg viewBox="0 0 226 226" aria-hidden="true">
        <circle cx="113" cy="113" r="107" fill="none" stroke="var(--track)" stroke-width="6"/>
        <circle cx="113" cy="113" r="107" fill="none" stroke="var(--accent)" stroke-width="6" pathLength="100" stroke-dasharray="50 100" transform="rotate(-90 113 113)"/>
      </svg>
      <div class="stat-value">50</div>
    </div>
    <div class="stat-label">MEETING</div>
  </section>

  <div class="prompt">CLICK TO CONTINUE</div>
  <svg class="mouse-icon" width="12" height="18" viewBox="0 0 12 18" aria-hidden="true">
    <rect x="1" y="1" width="10" height="16" rx="5" fill="none" stroke="#9a9a9a" stroke-width="1"/>
    <line x1="6" y1="4" x2="6" y2="7" stroke="#9a9a9a" stroke-width="1"/>
  </svg>
</main>
</body>
</html>
```